Dental Practice - Smiles Ahead - Corvell Walk - requires New Patient Flyer

We need a flyer to tell prospecting new patients about a new patient offer in our practice, Themed with black and whitewith a bit of colour, and using black and white stripes if possible.
We want to look empathetic, modern and appeal to adults.
The offer is for a complete comprehensive dental examination including all necessary x-rays with no out of pocket expense

Target Market(s)

adults, in particular 30-60 year olds

Industry/Entity Type

Dental

Font styles to use
Sans Serif

Colors
000000
ffffff
cee9f5

Requirements
Must have
• Smiles Ahead
• We are located in the heart of city Adelaide, along the iconic Corvell Walk.
• Dentist
• Complete comprehensive dental examination including all necessary x-rays
• with $0 out of pocket expense if you have dental health cover.
• No Health fund? We will do it all for you $95.
• With over 50 years combined experience, Dr Peter Halvorsen and Dr Wesley Tunbridge can offer all areas of dental treatment including Preventative, Whitening, Children, General, Cosmetic, Removal, Sedation and Implants.
• (08) 8564 3097
• frontdesk@brightquaydental.com.au
• Level 2, 17 Corvell Walk Adelaide SA 5000
• Please try and include all 3 pictures attached
Nice to have
• Partner Plus with KOVA, Accept all health funds, claim on the spot with MEDSWIPE
Should not have
• colour red, someone not smiling, someone in pain, photo of bad teeth/smile

```html
<!DOCTYPE html>
<html lang="en">
<head>
<meta charset="utf-8">
<title>Smiles Ahead – New Patient Flyer</title>
<link href="https://fonts.googleapis.com/css2?family=Roboto:ital,wght@0,300;0,400;0,700;1,700;1,900&family=Roboto+Condensed:wght@400;700&display=swap" rel="stylesheet">
<style>
  :root{
    --black:#000000;
    --white:#ffffff;
    --sky:#7fcbf0;
    --sky-pale:#cee9f5;
    --sky-mid:#a9dcf5;
    --fund-blue:#3d9bd8;
    --map-tone:#dcdad4;
    --page-bg:#efefef;
  }
  *{box-sizing:border-box;margin:0;padding:0}
  html,body{width:1200px;height:999px;overflow:hidden;background:var(--page-bg)}
  body{position:relative;font-family:"Roboto",Arial,sans-serif}
  .flyer{position:absolute;left:267px;top:38px;width:653px;height:927px;background:var(--white);overflow:hidden}
  .abs{position:absolute}
  .hero-photo{left:0;top:0;width:283px;height:307px;
    background:radial-gradient(ellipse at 55% 45%,#f1d8c8 0%,#e6bfa8 45%,#fbf6f2 100%)}
  .offer-panel{left:283px;top:0;width:370px;height:307px;background:var(--sky);text-align:center}
  .offer-title{margin-top:56px;font-weight:300;font-size:40px;line-height:40px;font-variant:small-caps;color:var(--black);letter-spacing:1px}
  .offer-sub{margin-top:22px;font-size:13px;letter-spacing:2.4px;color:var(--sky-pale);font-weight:400}
  .info-band{left:0;top:315px;width:653px;height:269px;background:var(--black)}
  .brand-oval{left:45px;top:251px;width:300px;height:180px;border-radius:50%;background:var(--white);
    box-shadow:-8px 8px 0 var(--sky-mid);
    display:flex;align-items:center;justify-content:center}
  .brand-name{font-weight:700;font-size:32px;color:var(--black)}
  .phone-pill{left:345px;top:378px;width:308px;height:60px;border-radius:22px 0 0 22px;
    background:linear-gradient(90deg,var(--sky-mid),var(--sky-pale) 70%,var(--white));padding-left:10px}
  .phone-number{display:inline-block;font-family:"Roboto Condensed",Arial,sans-serif;font-weight:700;font-size:48px;line-height:60px;
    color:var(--black);transform:scaleX(.76);transform-origin:left center;white-space:nowrap}
  .experience{left:0;top:454px;width:653px;text-align:center;color:var(--white);font-size:21px;line-height:24px;font-weight:300}
  .experience .sc{font-variant:small-caps}
  .services{display:block;color:var(--sky);font-weight:900;font-style:italic;font-variant:small-caps;font-size:23px;line-height:26px;letter-spacing:.5px}
  .card{border-radius:14px;background:linear-gradient(90deg,var(--sky-mid),var(--sky-pale) 55%,var(--sky-mid));
    box-shadow:0 0 0 4px var(--sky-pale);overflow:hidden}
  .card-cover{left:33px;top:612px;width:377px;height:110px}
  .card-photo{position:absolute;top:6px;bottom:6px;border-radius:10px}
  .cover-photo{left:6px;width:122px;background:linear-gradient(135deg,#d9c3b2,#f3e7dd 55%,#b9d4e0)}
  .cover-text{position:absolute;left:134px;right:8px;top:10px;text-align:center;font-size:19px;line-height:20px;color:var(--black)}
  .cover-text .zero{font-weight:700;font-size:36px;letter-spacing:-2px}
  .cover-text small{display:block;font-size:12px;line-height:16px;margin-top:2px;font-family:"Roboto Condensed",Arial,sans-serif}
  .card-white{left:33px;top:731px;width:271px;height:110px}
  .white-photo{right:6px;width:100px;background:linear-gradient(160deg,#f2e4da,#c79f84 55%,#7a5a48)}
  .white-text{position:absolute;left:6px;width:152px;top:26px;text-align:center;font-size:18px;line-height:20px}
  .funds-disc{left:429px;top:602px;width:106px;height:106px;border-radius:50%;background:var(--black);
    box-shadow:-2px 5px 0 var(--sky-mid);color:var(--white);text-align:center;
    font-family:"Roboto Condensed",Arial,sans-serif;font-size:14px;line-height:17px;padding-top:12px}
  .fund-square{left:555px;top:615px;width:70px;height:69px;background:var(--fund-blue)}
  .fund-name{left:548px;top:686px;width:84px;text-align:center;font-size:9px;font-weight:700;color:var(--fund-blue);letter-spacing:.3px}
  .location{left:318px;top:733px;width:98px;text-align:right;font-family:"Roboto Condensed",Arial,sans-serif;font-size:14px;line-height:18px;color:#444}
  .location strong{color:var(--black);font-weight:400}
  .map{left:425px;top:730px;width:208px;height:110px;border:3px solid var(--white);box-shadow:0 0 4px rgba(0,0,0,.3);
    background:linear-gradient(135deg,#e4e2dc,var(--map-tone))}
  .footer{left:0;top:855px;width:653px;height:39px;background:linear-gradient(90deg,#000 0%,#555 45%,#9a9a9a 60%,#000 100%);
    color:var(--sky-pale);font-family:"Roboto Condensed",Arial,sans-serif;font-weight:700;font-size:18px;line-height:39px;text-align:center;white-space:nowrap}
</style>
</head>
<body>
  <main class="flyer">
    <div class="abs hero-photo" role="img" aria-label="Photo of a smiling woman with short hair"></div>
    <section class="abs offer-panel">
      <h1 class="offer-title">Complete<br>Comprehensive<br>Dental<br>Examination</h1>
      <p class="offer-sub">INCLUDING ALL NECESSARY X-RAYS</p>
    </section>

    <section class="abs info-band"></section>
    <div class="abs brand-oval"><span class="brand-name">Smiles Ahead</span></div>
    <div class="abs phone-pill"><span class="phone-number">(08) 8564 3097</span></div>
    <p class="abs experience">With over 50 years combined experience,<br>
      <span class="sc">Dr Peter Halvorsen</span> and <span class="sc">Dr Wesley Tunbridge</span> can offer all<br>
      areas of dental treatment including
      <span class="services">Preventative, Whitening, Children, General,<br>Cosmetic, Removal, Sedation and Implants.</span>
    </p>

    <div class="abs card card-cover">
      <div class="card-photo cover-photo" role="img" aria-label="Photo of a smiling patient in a dental chair"></div>
      <p class="cover-text">With <span class="zero">$0</span> out of pocket expense if you have dental health cover.
        <small>No Health fund? We will do it all for you $95.</small></p>
    </div>

    <div class="abs funds-disc">ACCEPT all<br>health funds,<br>claim on the<br>spot with<br>MEDSWIPE</div>
    <div class="abs fund-square"></div>
    <div class="abs fund-name">PARTNER PLUS</div>

    <div class="abs card card-white">
      <p class="white-text">Get <strong>“WOW”</strong><br>Whitening Results,<br>Today!</p>
      <div class="card-photo white-photo" role="img" aria-label="Photo of a smiling young woman with brown hair"></div>
    </div>

    <p class="abs location">WE ARE<br>LOCATED in<br>the heart of<br>city Adelaide,<br>along the iconic<br><strong>CORVELL WALK.</strong></p>
    <div class="abs map" role="img" aria-label="Street map of central Adelaide with a pin on Corvell Walk"></div>

    <footer class="abs footer">Level 2, 17 Corvell Walk Adelaide SA 5000 • frontdesk@brightquaydental.com.au</footer>
  </main>
</body>
</html>
```